Ledgerwise Business Card Design

Business Card Design for new business called Ledgerwise focused on selling business software to small and medium size companies who have outgrown Tallymark. Similar companies would be Tallymark, Nuvo, CoreFlow. Also Dealharbor would be good to look at for additional ideas around look and feel.

Target Market(s)

Business to Business

Industry/Entity Type

Information Technology

Contact Information for Business Card

Standard Business Card Information

Font styles to use
Sans Serif

```html
<!DOCTYPE html>
<html lang="en">
<head>
<meta charset="utf-8">
<title>Ledgerwise Business Card</title>
<link rel="stylesheet" href="https://fonts.googleapis.com/css2?family=Open+Sans:wght@400;700&display=swap">
<style>
  :root {
    --brand-blue: #0b4f83;
    --brand-orange: #f28322;
    --ink: #1c1c1c;
    --paper: #ffffff;
    --backdrop: #ececec;
  }
  * { margin: 0; padding: 0; box-sizing: border-box; }
  html, body {
    width: 1189px; height: 1200px; overflow: hidden;
    background: var(--backdrop);
    font-family: "Open Sans", Arial, sans-serif;
  }
  .card {
    position: absolute; left: 140px; width: 917px; height: 524px;
    background: var(--paper); overflow: hidden;
    box-shadow: 0 3px 10px rgba(0,0,0,0.18);
  }
  .card--front { top: 45px; }
  .card--back { top: 623px; }

  .holder { position: absolute; left: 37px; top: 56px; }
  .holder__name { color: var(--brand-blue); font-size: 42px; line-height: 1.1; font-weight: 400; }
  .holder__role { color: var(--ink); font-size: 23px; line-height: 1.2; }

  .contact { position: absolute; left: 38px; top: 221px; list-style: none; }
  .contact__item { display: flex; align-items: center; height: 39px; font-size: 25px; color: var(--ink); }
  .contact__icon {
    width: 23px; height: 23px; margin-right: 26px; background: var(--brand-blue);
    display: flex; align-items: center; justify-content: center; flex: none;
  }
  .contact__icon svg { width: 15px; height: 15px; }
  .address { position: absolute; left: 37px; top: 386px; font-size: 25px; line-height: 34px; color: var(--ink); }

  .wave { position: absolute; left: 0; top: 0; width: 100%; height: 100%; }

  .wordmark { position: absolute; display: flex; align-items: center; gap: 14px; }
  .wordmark__dot { border-radius: 50%; background: var(--brand-orange); flex: none; }
  .wordmark__name { color: var(--brand-blue); font-weight: 700; letter-spacing: -1px; line-height: 1; }
  .card--front .wordmark { right: 54px; top: 150px; }
  .card--front .wordmark__dot { width: 40px; height: 40px; }
  .card--front .wordmark__name { font-size: 62px; }
  .card--back .wordmark { left: 110px; top: 170px; }
  .card--back .wordmark__dot { width: 58px; height: 58px; }
  .card--back .wordmark__name { font-size: 88px; }

  .accent-disc {
    position: absolute; left: 702px; top: 292px; width: 196px; height: 196px;
    border-radius: 50%; background: var(--brand-orange); opacity: 0.18;
  }
</style>
</head>
<body>
  <section class="card card--front">
    <svg class="wave" viewBox="0 0 1124 642" preserveAspectRatio="none" aria-hidden="true">
      <path d="M0,560 C400,600 850,560 1124,372 L1124,388 C900,512 500,616 0,622 Z" fill="var(--brand-blue)"/>
      <path d="M0,632 C500,626 900,522 1124,400 L1124,642 L0,642 Z" fill="var(--brand-orange)"/>
    </svg>

    <div class="holder">
      <p class="holder__name">Rowan Alcott</p>
      <p class="holder__role">Owner</p>
    </div>

    <div class="wordmark">
      <span class="wordmark__dot"></span>
      <span class="wordmark__name">Ledgerwise</span>
    </div>

    <ul class="contact">
      <li class="contact__item">
        <span class="contact__icon"><svg viewBox="0 0 16 16"><rect x="4" y="1" width="8" height="14" rx="1.5" fill="none" stroke="#fff" stroke-width="1.5"/><rect x="6" y="4" width="4" height="5" fill="#fff"/></svg></span>
        0412 308 764
      </li>
      <li class="contact__item">
        <span class="contact__icon"><svg viewBox="0 0 16 16"><path d="M4 1 L6.5 4.5 L5 6.5 Q6.5 9.5 9.5 11 L11.5 9.5 L15 12 L13 15 Q5 14 1 3 Z" fill="#fff"/></svg></span>
        07 5523 4170
      </li>
      <li class="contact__item">
        <span class="contact__icon"><svg viewBox="0 0 16 16"><rect x="1" y="3.5" width="14" height="9" fill="none" stroke="#fff" stroke-width="1.5"/><path d="M1 3.5 L8 9 L15 3.5" fill="none" stroke="#fff" stroke-width="1.5"/></svg></span>
        hello@ledgerwise.com
      </li>
      <li class="contact__item">
        <span class="contact__icon"><svg viewBox="0 0 16 16"><circle cx="8" cy="8" r="6.5" fill="none" stroke="#fff" stroke-width="1.5"/><path d="M1.5 8 H14.5 M8 1.5 Q4 8 8 14.5 M8 1.5 Q12 8 8 14.5" fill="none" stroke="#fff" stroke-width="1.2"/></svg></span>
        www.ledgerwise.com
      </li>
    </ul>

    <p class="address">428 Alder St, Ste C Fairview, CO 80612</p>
  </section>

  <section class="card card--back">
    <div class="wordmark">
      <span class="wordmark__dot"></span>
      <span class="wordmark__name">Ledgerwise</span>
    </div>
    <span class="accent-disc" aria-hidden="true"></span>
  </section>
</body>
</html>
```